Bluestone Freight

We are a 3PL freight brokerage company looking to create a website to attract new customers. Some ideas on how other freight websites look is located at these links, https://www.marigoldhaulerline.com/services, https://quillmarkcargo.com/freight-brokerage/.
We would like to have a quote feature implemented into this website.

We specialize in heavy-haul, specialized loads, flatbed, and dry vans.

```html
<!DOCTYPE html>
<html lang="en">
<head>
<meta charset="utf-8">
<title>Bluestone Freight</title>
<link href="https://fonts.googleapis.com/css2?family=Russo+One&family=Poppins:ital,wght@0,400;0,500;0,600;0,700;1,400&display=swap" rel="stylesheet">
<style>
:root{
  --navy:#13294b;
  --navy-deep:#0c1b33;
  --gold:#c39a2b;
  --gold-dark:#a98322;
  --ink:#222831;
  --text:#555b66;
  --light:#f4f5f7;
  --white:#ffffff;
  --line:#c9ccd3;
}
*{box-sizing:border-box;margin:0;padding:0}
html,body{width:1200px;height:5282px;overflow:hidden}
body{font-family:"Poppins",sans-serif;color:var(--text);background:var(--white);position:relative}
.heading{font-family:"Russo One",sans-serif;text-transform:uppercase;letter-spacing:1px}
.abs{position:absolute}
section,header,footer{position:absolute;left:0;width:1200px}
.eyebrow{color:var(--gold);font-family:"Russo One",sans-serif;font-size:25px;text-transform:uppercase}
.title{color:var(--navy);font-family:"Russo One",sans-serif;font-size:38px;text-transform:uppercase;display:flex;align-items:center;gap:8px;white-space:nowrap}
.rule{display:block;width:140px;height:10px;border-top:3px solid var(--navy);border-bottom:2px solid var(--navy);margin-top:8px}
.center{text-align:center}
.center .title{justify-content:center}
.center .rule{margin:8px auto 0}
.btn{display:inline-block;background:var(--gold);color:#fff;font-size:13px;font-weight:600;text-transform:uppercase;padding:10px 18px;border-radius:8px;white-space:nowrap}
.more{color:var(--gold);font-size:12px;font-weight:600;text-transform:uppercase}
p{font-size:11px;line-height:20px}

/* top bar */
.topbar{top:0;height:33px;background:var(--gold)}
.topbar .left{position:absolute;left:0;top:0;height:33px;width:640px;background:var(--navy);clip-path:polygon(0 0,100% 0,96% 100%,0 100%)}
.topbar .item{position:absolute;top:6px;color:#fff;font-size:10px;font-weight:500;display:flex;align-items:center;gap:10px;white-space:nowrap}
.dot{width:20px;height:20px;border-radius:50%;border:1.5px solid #fff;display:inline-block}
.dot.gold{background:var(--gold);border:none}
/* header */
.site-header{top:33px;height:84px;background:#fff}
.brand{position:absolute;left:130px;top:28px;color:var(--navy);font-family:"Poppins",sans-serif;font-weight:700;font-size:17px;display:flex;align-items:center;gap:8px;text-transform:uppercase;white-space:nowrap}
.brand .sq{width:16px;height:16px;background:var(--navy)}
.nav{position:absolute;left:308px;top:36px;display:flex;gap:32px;font-size:10px;font-weight:600;color:var(--ink);text-transform:uppercase;white-space:nowrap}
.call{position:absolute;left:880px;top:24px;display:flex;align-items:center;gap:8px;white-space:nowrap}
.call small{display:block;color:var(--gold);font-size:8px;font-weight:600;text-transform:uppercase}
.call b{color:var(--navy);font-size:21px;font-weight:700}
/* hero */
.hero{top:117px;height:600px}
.hero h1{position:absolute;left:130px;top:150px;color:#fff;font-family:"Russo One",sans-serif;font-size:52px;line-height:64px;white-space:nowrap}
.photo{position:absolute}
.cols{position:absolute;display:flex}
.col{text-align:center}
.col h3{font-family:"Russo One",sans-serif;color:var(--navy);font-size:15px;text-transform:uppercase;margin:14px 0 6px}
.blog-card h3{font-family:"Poppins",sans-serif;font-weight:700;color:var(--ink);font-size:13px;line-height:18px;text-transform:uppercase;margin:6px 0 8px}
.date{color:var(--gold);font-size:9px;font-weight:600;text-transform:uppercase}
.field{position:absolute;border:1.5px solid var(--line);border-radius:10px;font-size:9px;color:#666;padding:16px 10px 0}
.footer h4{font-family:"Russo One",sans-serif;color:#fff;font-size:15px;text-transform:uppercase;margin-bottom:18px}
.footer ul{list-style:none;color:#fff;font-size:11px}
.footer li{height:25px;display:flex;gap:10px;align-items:center}
.footer li::before{content:"»";color:#fff}
.footer ul.plain li::before{content:"";width:8px;height:8px;background:#fff;border-radius:50%}
</style>
</head>
<body>

<div class="abs topbar">
  <div class="left"></div>
  <div class="item" style="left:130px"><span class="dot gold"></span>123 Lorem ipsum dolor sit amet consectetur adipiscing elit.</div>
  <div class="item" style="left:670px"><span class="dot" style="background:#fff"></span>hello@bluestonefreight.example</div>
  <div class="item" style="left:940px;gap:8px"><span class="dot"></span><span class="dot"></span><span class="dot"></span><span class="dot"></span></div>
</div>

<header class="site-header">
  <div class="brand"><span class="sq"></span>Bluestone Freight</div>
  <nav class="nav"><span>Home</span><span>Services</span><span>About</span><span>Carriers</span><span>Resources</span><span>Race Team</span><span>Contact Us</span></nav>
  <div class="call">
    <svg width="34" height="34" viewBox="0 0 34 34"><circle cx="17" cy="17" r="17" fill="#13294b"/><path d="M12 10l3 0 1.5 4-2 1.3a9 9 0 0 0 4.2 4.2l1.3-2 4 1.5v3c0 1-1 2-2 2-7 0-13-6-13-13 0-1 1-2 2-2z" fill="#fff"/></svg>
    <div><small>Give us a call</small><b>555 014 2236</b></div>
  </div>
</header>

<section class="hero">
  <svg width="1200" height="600" style="position:absolute;left:0;top:0">
    <defs>
      <linearGradient id="heroG" x1="0" y1="0" x2="1" y2="1"><stop offset="0" stop-color="#4d5a52"/><stop offset=".5" stop-color="#6b7480"/><stop offset="1" stop-color="#2d3f6d"/></linearGradient>
    </defs>
    <rect width="1200" height="600" fill="url(#heroG)" role="img" aria-label="Blue semi truck hauling heavy equipment on a forest road"/>
    <polygon points="100,0 330,0 60,520" fill="#c39a2b" opacity=".45"/>
    <polygon points="380,0 620,0 440,330" fill="#c39a2b" opacity=".35"/>
    <path d="M0,600 L0,480 Q600,610 1200,480 L1200,600Z" fill="#fff"/>
    <path d="M10,485 L640,580 L600,590 Z" fill="#c39a2b"/>
    <path d="M600,590 L1200,480 L1200,500 L640,600Z" fill="#13294b"/>
    <circle cx="572" cy="540" r="5" fill="#fff"/><circle cx="590" cy="540" r="5" fill="none" stroke="#fff" stroke-width="1.5"/><circle cx="608" cy="540" r="5" fill="none" stroke="#fff" stroke-width="1.5"/><circle cx="626" cy="540" r="5" fill="none" stroke="#fff" stroke-width="1.5"/>
  </svg>
  <h1>Grow Your Business<br>With Bluestone<br>Freight</h1>
  <span class="btn abs" style="left:130px;top:357px">Get Started</span>
</section>

<section style="top:717px;height:653px">
  <div class="photo" style="left:100px;top:65px;width:500px;height:480px;background:linear-gradient(135deg,#b58a2a,#8a7a5c 50%,#5b5348)" role="img" aria-label="Photo collage of yellow heavy machinery and flatbed trucks"></div>
  <div class="abs" style="left:630px;top:70px">
    <div class="eyebrow">Welcome to</div>
    <div class="title">Bluestone Freight <span style="color:var(--gold)">»</span></div>
    <span class="rule"></span>
  </div>
  <div class="abs" style="left:630px;top:180px;width:470px">
    <p>Lorem ipsum dolor sit amet, consectetur adipiscing elit, sed do eiusmod tempor incididunt ut labore et dolore magna aliqua. Quis ipsum suspendisse ultrices gravida. Risus commodo viverra maecenas accumsan lacus vel facilisis. Lorem ipsum dolor sit amet, consectetur adipiscing elit, sed do eiusmod tempor incididunt ut labore et dolore magna aliqua. Ut enim ad minim veniam, quis nostrud exercitation ullamco laboris nisi ut aliquip ex ea commodo consequat. Duis aute irure dolor in reprehenderit in voluptate.</p>
    <p style="margin-top:18px">Velit esse cillum dolore eu fugiat nulla pariatur. Excepteur sint occaecat cupidatat non proident, sunt in culpa qui officia deserunt mollit anim id est laborum. Sed ut perspiciatis unde omnis iste natus error sit voluptatem accusantium doloremque laudantium, totam rem aperiam, eaque ipsa quae ab illo inventore veritatis et quasi architecto beatae vitae dicta sunt explicabo. Nemo enim ipsam voluptatem quia voluptas sit aspernatur aut odit aut fugit, sed quia consequuntur magni dolores eos qui ratione voluptatem sequi nesciunt. Neque porro quisquam est, qui dolorem ipsum quia dolor sit amet.</p>
    <span class="btn" style="margin-top:22px">Learn More About Us</span>
  </div>
</section>

<section style="top:1370px;height:560px;background:var(--light)" class="center">
  <div style="padding-top:63px">
    <div class="eyebrow">Why Choose</div>
    <div class="title">Bluestone Freight <span style="color:var(--gold)">»</span></div>
    <span class="rule"></span>
  </div>
  <div class="cols" style="left:130px;top:200px;gap:40px">
    <div class="col" style="width:290px">
      <svg width="120" height="138" viewBox="0 0 120 138"><polygon points="60,2 118,35 118,103 60,136 2,103 2,35" fill="#13294b"/><polygon points="60,10 111,39 111,99 60,128 9,99 9,39" fill="none" stroke="#fff" stroke-width="1.5" stroke-dasharray="3 3"/><rect x="40" y="44" width="40" height="44" rx="5" fill="none" stroke="#fff" stroke-width="3"/><line x1="40" y1="64" x2="80" y2="64" stroke="#fff" stroke-width="3"/><circle cx="48" cy="78" r="3" fill="#fff"/><circle cx="72" cy="78" r="3" fill="#fff"/></svg>
      <h3>Lorem Ipsum Dolor</h3>
      <p>Lorem ipsum dolor sit amet, consectetur adipiscing elit, sed do eiusmod tempor incididunt ut labore et dolore magna aliqua. Quis ipsum suspendisse ultrices gravida. Risus commodo viverra maecenas.</p>
      <div class="more" style="margin-top:12px">Learn More</div>
    </div>
    <div class="col" style="width:290px">
      <svg width="120" height="138" viewBox="0 0 120 138"><polygon points="60,2 118,35 118,103 60,136 2,103 2,35" fill="#13294b"/><polygon points="60,10 111,39 111,99 60,128 9,99 9,39" fill="none" stroke="#fff" stroke-width="1.5" stroke-dasharray="3 3"/><rect x="42" y="42" width="36" height="50" rx="4" fill="none" stroke="#fff" stroke-width="3"/><rect x="48" y="48" width="24" height="14" fill="none" stroke="#fff" stroke-width="2"/><line x1="46" y1="72" x2="74" y2="72" stroke="#fff" stroke-width="2"/><line x1="46" y1="80" x2="74" y2="80" stroke="#fff" stroke-width="2"/></svg>
      <h3>Lorem Ipsum Dolor</h3>
      <p>Lorem ipsum dolor sit amet, consectetur adipiscing elit, sed do eiusmod tempor incididunt ut labore et dolore magna aliqua. Quis ipsum suspendisse ultrices gravida. Risus commodo viverra maecenas.</p>
      <div class="more" style="margin-top:12px">Learn More</div>
    </div>
    <div class="col" style="width:290px">
      <svg width="120" height="138" viewBox="0 0 120 138"><polygon points="60,2 118,35 118,103 60,136 2,103 2,35" fill="#13294b"/><polygon points="60,10 111,39 111,99 60,128 9,99 9,39" fill="none" stroke="#fff" stroke-width="1.5" stroke-dasharray="3 3"/><rect x="30" y="52" width="40" height="28" fill="none" stroke="#fff" stroke-width="3"/><path d="M70 60h12l8 10v10H70z" fill="none" stroke="#fff" stroke-width="3"/><circle cx="42" cy="84" r="5" fill="#13294b" stroke="#fff" stroke-width="3"/><circle cx="80" cy="84" r="5" fill="#13294b" stroke="#fff" stroke-width="3"/></svg>
      <h3>Lorem Ipsum Dolor</h3>
      <p>Lorem ipsum dolor sit amet, consectetur adipiscing elit, sed do eiusmod tempor incididunt ut labore et dolore magna aliqua. Quis ipsum suspendisse ultrices gravida. Risus commodo viverra maecenas.</p>
      <div class="more" style="margin-top:12px">Learn More</div>
    </div>
  </div>
</section>

<section style="top:1930px;height:565px">
  <svg width="1200" height="565" style="position:absolute;left:0;top:0">
    <defs><linearGradient id="qG" x1="0" y1="0" x2="1" y2="0"><stop offset="0" stop-color="#1f4fb0"/><stop offset=".45" stop-color="#2456bd"/><stop offset=".6" stop-color="#6f7d93"/><stop offset="1" stop-color="#9a3c4a"/></linearGradient></defs>
    <rect width="1200" height="565" fill="url(#qG)" role="img" aria-label="Car carrier truck loaded with vehicles"/>
    <polygon points="0,0 560,0 440,565 0,565" fill="#1c47a8" opacity=".85"/>
    <line x1="210" y1="0" x2="0" y2="440" stroke="#c39a2b" stroke-width="2"/>
    <line x1="560" y1="0" x2="440" y2="565" stroke="#c39a2b" stroke-width="2"/>
  </svg>
  <h2 class="abs heading" style="left:160px;top:110px;color:#fff;font-size:54px;line-height:64px;letter-spacing:2px;white-space:nowrap">Quality &amp;<br>Trust Meet<br>Value</h2>
  <p class="abs" style="left:160px;top:310px;width:310px;color:#fff">Lorem ipsum dolor sit amet, consectetur adipiscing elit, sed do eiusmod tempor incididunt ut labore et dolore magna aliqua. Quis ipsum suspendisse ultrices gravida. Risus commodo viverra maecenas accumsan lacus vel facilisis.</p>
  <span class="btn abs" style="left:160px;top:408px">Contact Us</span>
</section>

<section style="top:2495px;height:470px;background:var(--light)" class="center">
  <div style="padding-top:68px">
    <div class="title"><span style="color:var(--gold)">Our</span> Services <span style="color:var(--gold)">»</span></div>
    <span class="rule"></span>
  </div>
  <div class="cols" style="left:110px;top:170px;gap:26px">
    <div class="col" style="width:226px">
      <svg width="92" height="106" viewBox="0 0 120 138"><polygon points="60,2 118,35 118,103 60,136 2,103 2,35" fill="#13294b"/><polygon points="60,10 111,39 111,99 60,128 9,99 9,39" fill="none" stroke="#fff" stroke-width="1.5" stroke-dasharray="3 3"/><rect x="22" y="58" width="52" height="18" fill="none" stroke="#fff" stroke-width="3"/><path d="M74 58h14l10 10v8H74z" fill="none" stroke="#fff" stroke-width="3"/><circle cx="34" cy="80" r="5" fill="#fff"/><circle cx="88" cy="80" r="5" fill="#fff"/></svg>
      <h3 style="font-size:12px">Heavy-Haul</h3>
      <p style="font-size:9.5px;line-height:18px">Lorem ipsum dolor sit amet, consectetur adipiscing elit, sed do eiusmod tempor incididunt ut labore et dolore magna aliqua.</p>
      <div class="more" style="margin-top:6px;font-size:10px">Learn More</div>
    </div>
    <div class="col" style="width:226px">
      <svg width="92" height="106" viewBox="0 0 120 138"><polygon points="60,2 118,35 118,103 60,136 2,103 2,35" fill="#13294b"/><polygon points="60,10 111,39 111,99 60,128 9,99 9,39" fill="none" stroke="#fff" stroke-width="1.5" stroke-dasharray="3 3"/><rect x="30" y="50" width="40" height="30" fill="none" stroke="#fff" stroke-width="3"/><path d="M70 58h12l8 10v12H70z" fill="none" stroke="#fff" stroke-width="3"/><circle cx="42" cy="84" r="5" fill="#fff"/><circle cx="80" cy="84" r="5" fill="#fff"/></svg>
      <h3 style="font-size:12px">Specialized Loads</h3>
      <p style="font-size:9.5px;line-height:18px">Lorem ipsum dolor sit amet, consectetur adipiscing elit, sed do eiusmod tempor incididunt ut labore et dolore magna aliqua.</p>
      <div class="more" style="margin-top:6px;font-size:10px">Learn More</div>
    </div>
    <div class="col" style="width:226px">
      <svg width="92" height="106" viewBox="0 0 120 138"><polygon points="60,2 118,35 118,103 60,136 2,103 2,35" fill="#13294b"/><polygon points="60,10 111,39 111,99 60,128 9,99 9,39" fill="none" stroke="#fff" stroke-width="1.5" stroke-dasharray="3 3"/><line x1="22" y1="74" x2="74" y2="74" stroke="#fff" stroke-width="4"/><path d="M74 56h12l10 10v10H74z" fill="none" stroke="#fff" stroke-width="3"/><circle cx="34" cy="82" r="5" fill="#fff"/><circle cx="86" cy="82" r="5" fill="#fff"/></svg>
      <h3 style="font-size:12px">Flatbed</h3>
      <p style="font-size:9.5px;line-height:18px">Lorem ipsum dolor sit amet, consectetur adipiscing elit, sed do eiusmod tempor incididunt ut labore et dolore magna aliqua.</p>
      <div class="more" style="margin-top:6px;font-size:10px">Learn More</div>
    </div>
    <div class="col" style="width:226px">
      <svg width="92" height="106" viewBox="0 0 120 138"><polygon points="60,2 118,35 118,103 60,136 2,103 2,35" fill="#13294b"/><polygon points="60,10 111,39 111,99 60,128 9,99 9,39" fill="none" stroke="#fff" stroke-width="1.5" stroke-dasharray="3 3"/><rect x="32" y="44" width="44" height="38" fill="none" stroke="#fff" stroke-width="3"/><path d="M76 58h10l8 10v14H76z" fill="none" stroke="#fff" stroke-width="3"/><circle cx="44" cy="86" r="5" fill="#fff"/><circle cx="84" cy="86" r="5" fill="#fff"/></svg>
      <h3 style="font-size:12px">Dry Vans</h3>
      <p style="font-size:9.5px;line-height:18px">Lorem ipsum dolor sit amet, consectetur adipiscing elit, sed do eiusmod tempor incididunt ut labore et dolore magna aliqua.</p>
      <div class="more" style="margin-top:6px;font-size:10px">Learn More</div>
    </div>
  </div>
</section>

<section style="top:2965px;height:685px" class="center">
  <div style="padding-top:65px">
    <div class="title"><span style="color:var(--gold)">Our</span> Latest Blog <span style="color:var(--gold)">»</span></div>
    <span class="rule"></span>
  </div>
  <div class="cols" style="left:130px;top:162px;gap:13px;text-align:left">
    <div class="blog-card" style="width:305px">
      <div style="height:190px;background:linear-gradient(180deg,#9db6cf,#8a7a5c 55%,#5b5b5b)" role="img" aria-label="Truck convoy on a desert highway"></div>
      <div style="padding:14px 10px"><div class="date">April 29 2022</div><h3>Lorem ipsum dolor sit amecon sectetur adipiscing elit.</h3><p style="font-size:10px;line-height:19px">Lorem ipsum dolor sit amet, consectetur adipiscing elit, sed do eiusmod tempor incididunt ut labore et dolore magna aliqua.</p><div class="more" style="margin-top:6px">Learn More</div></div>
    </div>
    <div class="blog-card" style="width:305px">
      <div style="height:190px;background:linear-gradient(180deg,#c7cfd6,#7d8185 60%,#4c4f52)" role="img" aria-label="Oversized cylindrical load on a trailer"></div>
      <div style="padding:14px 10px"><div class="date">April 29 2022</div><h3>Lorem ipsum dolor sit amecon sectetur adipiscing elit.</h3><p style="font-size:10px;line-height:19px">Lorem ipsum dolor sit amet, consectetur adipiscing elit, sed do eiusmod tempor incididunt ut labore et dolore magna aliqua.</p><div class="more" style="margin-top:6px">Learn More</div></div>
    </div>
    <div class="blog-card" style="width:305px">
      <div style="height:190px;background:linear-gradient(180deg,#6fa6e6,#c0384a 55%,#4f7a3b)" role="img" aria-label="Car carrier trailer on a country road"></div>
      <div style="padding:14px 10px"><div class="date">April 29 2022</div><h3>Lorem ipsum dolor sit amecon sectetur adipiscing elit.</h3><p style="font-size:10px;line-height:19px">Lorem ipsum dolor sit amet, consectetur adipiscing elit, sed do eiusmod tempor incididunt ut labore et dolore magna aliqua.</p><div class="more" style="margin-top:6px">Learn More</div></div>
    </div>
  </div>
  <span class="btn abs" style="left:510px;top:575px">View More All Blogs</span>
</section>

<section style="top:3650px;height:570px">
  <svg width="1200" height="570" style="position:absolute;left:0;top:0">
    <defs><linearGradient id="tG" x1="0" y1="0" x2="1" y2="0"><stop offset="0" stop-color="#8b8f94"/><stop offset=".45" stop-color="#4a5566"/><stop offset=".55" stop-color="#13294b"/><stop offset="1" stop-color="#13294b"/></linearGradient></defs>
    <rect width="1200" height="570" fill="url(#tG)" role="img" aria-label="Heavy transport truck carrying industrial machinery"/>
    <polygon points="880,0 1200,0 1200,210" fill="#c39a2b" opacity=".35"/>
  </svg>
  <div class="abs" style="left:598px;top:58px;color:#fff;white-space:nowrap">
    <div class="heading" style="font-size:25px">Our</div>
    <div class="heading" style="font-size:37px">Client Testimonial <span style="color:var(--gold)">»</span></div>
    <span class="rule" style="border-color:#fff"></span>
  </div>
  <div class="abs" style="left:600px;top:170px;width:470px;color:#fff;font-size:17px;line-height:31px;font-style:italic"><span style="font-size:40px;line-height:10px">“</span><br>Lorem ipsum dolor sit amet, consectetur adipiscing elit, sed do eiusmod tempor incididunt ut labore et dolore magna aliqua. Quis ipsum suspendisse ultrices gravida. Risus commodo viverra maecenas accumsan lacus vel facilisis. aliquip ex ea commodo consequat. Duis aute irure dolor in reprehenderit in voluptate velit esse cillum dolore eu fugiat nulla pariatur <span style="font-size:30px">”</span></div>
  <div class="abs" style="left:608px;top:472px;width:62px;height:62px;background:#8a95a6" role="img" aria-label="Client portrait"></div>
  <div class="abs" style="left:682px;top:486px;color:#fff;white-space:nowrap"><div class="heading" style="font-size:18px">Dana Whitlock</div><div style="font-size:10px">Lorem ipsum dolor</div></div>
</section>

<section style="top:4220px;height:680px">
  <div class="photo" style="left:100px;top:75px;width:500px;height:480px;background:linear-gradient(135deg,#c29a36,#8c7a52 50%,#4d4a44)" role="img" aria-label="Photo collage of a mining truck and a heavy load on a trailer"></div>
  <div class="abs" style="left:648px;top:98px">
    <div class="eyebrow">Contact Us</div>
    <div class="title">Request A Quote <span style="color:var(--gold)">»</span></div>
    <span class="rule"></span>
  </div>
  <div class="field" style="left:648px;top:227px;width:203px;height:42px">First Name</div>
  <div class="field" style="left:866px;top:227px;width:203px;height:42px">Last Name</div>
  <div class="field" style="left:648px;top:290px;width:203px;height:42px">Email Address</div>
  <div class="field" style="left:866px;top:290px;width:203px;height:42px">Phone Number</div>
  <div class="field" style="left:648px;top:352px;width:421px;height:98px;padding-top:10px">Message</div>
  <span class="btn abs" style="left:648px;top:477px;padding:11px 30px">Submit Now</span>
</section>

<footer class="footer" style="top:4860px;height:422px">
  <svg width="1200" height="422" style="position:absolute;left:0;top:0">
    <path d="M0,80 Q600,-20 1200,80 L1200,422 L0,422Z" fill="#0c1b33"/>
    <path d="M0,60 L610,0 L580,12 L0,72Z" fill="#13294b"/>
    <path d="M610,0 L1200,62 L1200,76 L640,10Z" fill="#c39a2b"/>
  </svg>
  <div class="abs" style="left:110px;top:218px;color:#fff;font-family:'Poppins',sans-serif;font-weight:700;font-size:24px;text-transform:uppercase;display:flex;align-items:center;gap:10px;white-space:nowrap"><span style="width:20px;height:20px;background:#fff;display:inline-block"></span>Bluestone Freight</div>
  <div class="abs" style="left:472px;top:110px"><h4>Quick Links</h4><ul><li>Home</li><li>Services</li><li>About</li><li>Carriers</li><li>Resources</li><li>Race Team</li><li>Contact Us</li></ul></div>
  <div class="abs" style="left:648px;top:110px"><h4>Follow Us</h4><ul class="plain"><li>Friendline</li><li>Snapgram</li><li>Chirper</li><li>Linkwork</li><li>Viewtube</li></ul></div>
  <div class="abs" style="left:830px;top:110px;color:#fff;font-size:11px;width:250px">
    <h4>Contact Us</h4>
    <div style="line-height:25px;padding-left:22px">123 Lorem ipsum dolor sit amet consectetur adipiscing.</div>
    <div style="line-height:25px;padding-left:22px;margin-top:10px">555 014 2236</div>
    <div style="line-height:25px;padding-left:22px;margin-top:14px">hello@bluestonefreight.example</div>
  </div>
  <div class="abs" style="left:100px;top:375px;width:1000px;border-top:1px solid #2c3a55"></div>
  <div class="abs" style="left:0;width:1200px;top:388px;text-align:center;color:#fff;font-size:10px">© copyrights 2022 Bluestone Freight &nbsp;&nbsp;|&nbsp;&nbsp; All rights reserved.</div>
</footer>

</body>
</html>
```